Visually Compelling Flyer Design - Harbor Perks

We are a life insurance company looking to create visually compelling flyers that gain attention of potential buyers and simplify the concept. It should be professional, friendly, approachable in nature. Our logo and several rough drafts are included.
We are looking to refine this look and make it ultra professional, clean and easy to follow. A creative brief with brand guidelines is also included.
FLYER 1 — PAY YOURSELF FIRST
EYEBROW TAG
YOUR COMPANY JUST UPGRADED YOUR BENEFITS
HEADLINE
One small decision. A lifetime of protection.
SUBHEADLINE
Permanent life insurance + long-term care coverage, starting at $1 a day.
EYEBROW TAG
CHOOSE YOUR DAILY INVESTMENT
STAT — TIER 1
$1 / day → $20,000 Life Insurance
STAT — TIER 2 (HERO — make this one biggest/most prominent)
$2 / day → $40,000 Life Insurance
★ Most Popular
STAT — TIER 3
$3 / day → $60,000 Life Insurance
CAPTION
Rate locked at enrollment. Benefit never decreases.
EYEBROW TAG
THREE BENEFITS. ONE POLICY.
SUBHEADLINE
Your money works three ways.
CALLOUT — BENEFIT 1
01 | Cash Value Growth
BODY
Averages 6% annually over the last 50 years — guaranteed never to fall below 3%. Better than any savings account. And if you ever need it, you can borrow against it. It's your money.
CALLOUT — BENEFIT 2
02 | Tax-Free Death Benefit
BODY
From day one, your family is protected. The full benefit is paid tax-free to the person you choose — no waiting period, no exceptions. That's your legacy, preserved.
CALLOUT — BENEFIT 3
03 | Long-Term Care Coverage
BODY
70% of Americans will need long-term care. This plan pays 75% of your benefit — upfront and tax-free — to cover those costs while you're still alive. Your retirement savings stay intact. Your family stays protected.
EYEBROW TAG
ALREADY HAVE LIFE INSURANCE THROUGH WORK?
SUBHEADLINE
That's term. It ends when you need it most.
BODY
Term life insurance is designed for temporary needs — protecting your paycheck, your mortgage, your kids while they're home. When you retire, the house is paid off and your children are grown. Term ends because the need ends.
BODY
But one need never ends: your final expenses and the cost of long-term care. This permanent plan stays with you after retirement — when term coverage is gone and getting new coverage is expensive or impossible.
COMPARISON — LEFT COLUMN HEADER
✕ TERM LIFE
COMPARISON — LEFT COLUMN ITEMS
Gets more expensive with age
Ends at retirement
No cash value
Temporary protection only
COMPARISON — RIGHT COLUMN HEADER
✓ THIS PLAN
COMPARISON — RIGHT COLUMN ITEMS
Rate locked forever at enrollment
Stays with you after retirement
Builds real cash value
Permanent protection for life
EYEBROW TAG
WHAT MAKES THIS DIFFERENT
SUBHEADLINE
Built for you. Stays with you.
CALLOUT
✓ Guaranteed Issued
No medical exams. No questions asked. You qualify.
CALLOUT
✓ Group Rate
Because you work here, you get pricing individuals can't access on their own.
CALLOUT
✓ Rate Locked Forever
Your premium never increases. Your benefit never decreases.
CALLOUT
✓ Portable
Change jobs. Retire. Your policy comes with you at the same rate.
CALLOUT
✓ Family Coverage
Protect your spouse and children under the same plan.
SUBHEADLINE
Protect retirement. Preserve dignity. Plan ahead.
CTA
Be on the lookout for your personalized coverage details.
CAPTION
Brokered by Harbor Perks · Underwritten by TrueLedger
FLYER 2 — THE LONG-TERM CARE REALITY
EYEBROW TAG
WHAT MOST PEOPLE DON'T KNOW — BUT SHOULD
HEADLINE
Most Americans are unprepared. You don't have to be.
SUBHEADLINE
The long-term care gap is real — and it affects families like yours.
EYEBROW TAG
THE NUMBERS ARE HARD TO IGNORE
STAT
70%
of Americans age 65 and older will need some form of long-term care during their lifetime.
CAPTION
Source: Pryce & Lomax, Review of Elder Welfare and Civic Planning, 2018
STAT
3–4%
of Americans over 50 own a private long-term care insurance policy. The gap between who needs it and who has it is staggering.
CAPTION
Source: Stroud & Bellamy, QVT Wellness Wire, 2023
STAT
$700 Billion+
Estimated annual U.S. long-term care cost — and it's growing every year.
CAPTION
Source: Delacroix Wynn & Pasternak, Civic Ledger Council, 2020
STAT
$470 Billion
The estimated value of unpaid care provided by family members every year. That's the real cost — measured in time, stress, and financial sacrifice.
CAPTION
Source: Tillman & Osei, Meridian Bureau
STAT
80%
of total long-term care spending goes directly to assist retirees. This isn't a young person's problem. But the time to plan is now.
CAPTION
SUBHEADLINE
Long-term care doesn't just cost money. It costs families.
BODY
When there's no plan in place, the people you love absorb the impact — financially, emotionally, and physically. Retirement savings built over a lifetime can disappear in months. Family members step back from their own lives to provide care. Dignity becomes a daily negotiation.
BODY
This is not inevitable. A small decision today changes the entire outcome.
EYEBROW TAG
THE SOLUTION
HEADLINE
The Pay Yourself First Principle.
BODY
Take the first $1, $2, or $3 you make every day and invest it in a permanent life insurance policy that includes long-term care coverage — underwritten by TrueLedger, offered through your employer at a group rate, and Guaranteed Issued for everyone.
STAT
$1 / day → $20,000 $2 / day → $40,000 $3 / day → $60,000
BODY
The benefit includes three protections in one: a cash value that grows at an average of 6% annually, a tax-free death benefit for your family, and long-term care coverage that pays 75% of your benefit upfront — tax-free — when you need care most.
SUBHEADLINE
Whether you're single, married, with children or without — there is protection in this plan for you.
HEADLINE
CTA
Look for your personalized offer. Coverage details are coming your way.
CAPTION
COPY RULES FOR DESIGNERS
Headlines are one idea only. Never more than two lines.
Stats stand alone. Never buried in a paragraph.
Body copy maxes at 3 sentences per block. If it's longer, cut it.
The $2/day tier is always the hero. Always.
"Guaranteed Issued" appears on both flyers. It's the most important trust signal.
TrueLedger is always attributed. Always.
The tagline is: Protect retirement. Preserve dignity. Plan ahead. — Use it verbatim.
Target Market(s)
Average Americans with a family - adults looking for life insurance
Industry/Entity Type
Life Insurance & Financial Retirement

```html
<!DOCTYPE html>
<html lang="en">
<head>
<meta charset="utf-8">
<title>Harbor Perks — Flyer Set</title>
<link href="https://fonts.googleapis.com/css2?family=Arimo:wght@400;700&family=Tinos:ital,wght@0,400;0,700;1,400&display=swap" rel="stylesheet">
<style>
:root{
  --blue:#1554a6;
  --blue-2:#0b57ae;
  --stripe:#7fa8d6;
  --panel:#e8f0f9;
  --panel-mid:#c9dcef;
  --page-bg:#e6eef8;
  --ink:#1d1d1d;
  --gray:#4a4f58;
  --white:#ffffff;
  --serif:"Tinos","Times New Roman",serif;
  --sans:"Arimo","Helvetica Neue",Arial,sans-serif;
}
*{box-sizing:border-box;margin:0;padding:0}
html,body{width:1200px;height:766px;overflow:hidden;background:#fff}
.canvas{position:relative;width:1200px;height:766px}
.flyer{position:absolute;top:29px;width:960px;height:1318px;transform:scale(.528);transform-origin:0 0;font-family:var(--sans);overflow:hidden}
.flyer *{position:absolute}
.flyer b,.flyer br{position:static}
.flyer--reality{left:75px;background:var(--white)}
.flyer--offer{left:613px;background:var(--page-bg)}
.serif{font-family:var(--serif);font-weight:700}
.eyebrow{font-weight:700;letter-spacing:3.5px;text-transform:uppercase}
.center{left:0;width:100%;text-align:center}

/* Reality flyer */
.r-header{left:0;top:0;width:960px;height:150px;background:var(--blue)}
.r-stripe{left:0;top:150px;width:960px;height:5px;background:var(--stripe)}
.r-title{left:55px;top:48px;font-size:34px;color:var(--white)}
.r-kicker{left:60px;top:91px;font-size:13px;color:var(--white)}
.r-brandline{left:600px;top:46px;width:330px;text-align:center;font-size:14px;color:var(--white);letter-spacing:3.5px;font-weight:400}
.r-brand{left:600px;top:69px;width:330px;text-align:center;font-size:22px;color:var(--white);letter-spacing:5px;font-weight:700}
.r-lede{left:60px;top:168px;font-size:34px;color:var(--blue)}
.r-sub{left:62px;top:222px;font-size:21px;color:var(--gray)}
.r-eyebrow{left:60px;top:268px;font-size:13px;color:var(--blue)}
.hero-stat{left:60px;top:307px;width:840px;height:116px;background:var(--blue);border-left:7px solid var(--stripe);border-radius:0 5px 5px 0}
.hero-stat .num{left:20px;top:6px;font-size:90px;color:var(--white);font-family:var(--serif);font-weight:700;line-height:1.1}
.hero-stat .lead{left:228px;top:16px;font-size:22px;color:var(--white);line-height:24px;width:600px}
.hero-stat .cite{left:228px;top:78px;font-size:21px;color:#d5e3f4;font-family:var(--serif);font-style:italic}
.stat-card{width:410px;height:138px;background:var(--panel);border-radius:4px}
.stat-card .bar{left:0;top:-3px;width:46px;height:4px;background:var(--blue)}
.stat-card .num{left:20px;top:10px;font-size:32px;color:var(--blue);font-family:var(--serif);font-weight:700}
.stat-card .label{left:20px;top:52px;font-size:14px;color:var(--blue);font-weight:700;letter-spacing:1.5px}
.stat-card .body{left:20px;top:72px;width:376px;font-size:13px;line-height:16px;color:var(--ink)}
.stat-card .cite{left:20px;top:118px;font-size:9.5px;color:var(--gray);font-family:var(--serif);font-style:italic}
.impact{left:60px;top:770px;width:840px;height:82px;background:var(--panel-mid);border-radius:4px}
.impact .head{left:20px;top:10px;font-size:20px;color:var(--blue)}
.impact .body{left:20px;top:38px;width:800px;font-size:14px;line-height:17px;color:var(--ink)}
.sol-eyebrow{left:66px;top:874px;font-size:12px;color:var(--blue)}
.sol-title{left:62px;top:892px;font-size:27px;color:var(--blue)}
.sol-body{left:63px;top:923px;width:850px;font-size:16.5px;line-height:20px;color:var(--ink)}
.tier{top:1015px;width:270px;height:84px;background:var(--panel);border:1.5px solid #d3e1f1;border-radius:4px;text-align:center}
.tier .rate{left:0;width:100%;top:8px;font-size:22px;color:var(--blue);font-family:var(--serif);font-weight:700}
.tier .amt{left:0;width:100%;top:50px;font-size:18px;color:var(--blue);font-weight:700}
.tier--hero{background:var(--blue);border-color:var(--blue)}
.tier--hero .rate,.tier--hero .amt{color:var(--white)}
.tier--hero .amt{top:42px}
.tier--hero .tag{left:0;width:100%;top:67px;font-size:10px;color:#d5e3f4;letter-spacing:3px;font-weight:700}
.sol-note{left:60px;top:1122px;width:840px;text-align:center;font-size:16.5px;line-height:20px;color:var(--ink)}
.r-footer{left:0;top:1186px;width:960px;height:132px;background:var(--blue);border-top:5px solid var(--stripe)}
.f-tag{top:26px;font-size:23px;color:var(--white)}
.f-cta{top:60px;font-size:21px;color:var(--white)}
.f-credit{top:95px;font-size:13px;color:#bcd2ec;letter-spacing:2.5px;font-weight:700}

/* Offer flyer */
.o-header{left:0;top:0;width:958px;height:183px;background:var(--blue-2)}
.o-stripe{left:0;top:183px;width:958px;height:7px;background:var(--stripe)}
.o-eyebrow{top:62px;font-size:15px;color:var(--white);letter-spacing:4px}
.o-title{top:84px;font-size:43px;line-height:42px;color:var(--white)}
.o-sub{top:224px;font-size:18px;color:var(--gray)}
.hero-card{left:66px;top:265px;width:828px;height:235px;background:var(--white);border:3px solid var(--blue-2);border-radius:12px}
.hero-card .badge{right:-3px;top:-3px;width:234px;height:38px;background:var(--blue-2);border-radius:0 12px 0 10px;color:var(--white);font-size:19px;letter-spacing:3px;font-weight:700;text-align:center;line-height:38px}
.hero-card .pick{top:44px;font-size:14px;color:var(--blue-2);letter-spacing:4px}
.hero-card .rate{top:52px;font-size:74px;line-height:84px;color:var(--blue-2)}
.hero-card .benefit{top:140px;font-size:20px;font-weight:700;color:var(--ink)}
.hero-card .note{top:176px;font-size:15px;color:var(--gray)}
.o-tier{top:513px;width:404px;height:92px;background:var(--panel-mid);border-radius:10px;text-align:center}
.o-tier .rate{left:0;width:100%;top:10px;font-size:28px;color:var(--blue-2);font-family:var(--serif);font-weight:700}
.o-tier .amt{left:0;width:100%;top:52px;font-size:17px;font-weight:700;color:var(--ink)}
.o-section{font-size:26px;color:var(--blue-2)}
.way{top:698px;width:265px;height:150px;background:var(--white);border:2px solid #c6d9ee;border-radius:8px}
.way .head{left:18px;top:26px;font-size:16px;color:var(--blue-2);letter-spacing:2.5px;font-weight:700;display:flex;align-items:center;gap:10px;position:absolute}
.way .head .dot{position:static;width:20px;height:20px;border-radius:50%;background:var(--blue-2);color:var(--white);font-size:12px;letter-spacing:0;text-align:center;line-height:20px}
.way .body{left:22px;top:62px;width:225px;font-size:15px;line-height:18px;color:var(--gray)}
.compare{top:929px;width:400px;height:166px;border-radius:8px}
.compare--term{left:66px;background:var(--panel-mid)}
.compare--plan{left:493px;background:var(--blue-2)}
.compare .head{left:0;width:100%;text-align:center;top:18px;font-size:17px;letter-spacing:3.5px;font-weight:700}
.compare--term .head{color:#3f5168}
.compare--plan .head{color:var(--white)}
.compare ul{left:44px;top:50px;list-style:none;font-size:16px;line-height:25px}
.compare ul li{position:static}
.compare--term ul{color:#3f5168}
.compare--plan ul{color:var(--white)}
.compare .tick{left:288px;top:52px;width:92px;height:92px}
.perk{top:1112px;width:265px;height:74px;background:var(--white);border:1.5px solid #c6d9ee;border-left:5px solid var(--blue-2);border-radius:6px;text-align:center}
.perk .head{left:0;width:100%;top:18px;font-size:15px;color:var(--blue-2);letter-spacing:2.5px;font-weight:700}
.perk .body{left:0;width:100%;top:39px;font-size:14px;color:var(--ink)}
.perk .body.small{font-size:12px;top:42px}
.o-footer{left:0;top:1196px;width:958px;height:122px;background:var(--blue-2);border-top:6px solid var(--stripe)}
.o-footer .f-tag{top:14px}
.o-footer .f-cta{top:52px;font-size:17px;font-weight:700}
.o-footer .f-credit{top:84px;font-size:13px}
</style>
</head>
<body>
<div class="canvas">

  <section class="flyer flyer--reality">
    <div class="r-header"></div>
    <div class="r-stripe"></div>
    <h1 class="r-title serif">Most Americans are unprepared.</h1>
    <p class="r-kicker eyebrow">What most people don't know — but should</p>
    <p class="r-brandline">LONG-TERM CARE REALITY</p>
    <p class="r-brand">HARBOR PERKS</p>

    <h2 class="r-lede serif">You don't have to be.</h2>
    <p class="r-sub">The long-term care gap is real — and it affects families like yours.</p>
    <p class="r-eyebrow eyebrow">The numbers are hard to ignore</p>

    <div class="hero-stat">
      <p class="num">70%</p>
      <p class="lead">of Americans 65+<br>will need some form of long-term care during their lifetime.</p>
      <p class="cite">Pryce &amp; Lomax, Review of Elder Welfare and Civic Planning, 2018</p>
    </div>

    <div class="stat-card" style="left:64px;top:452px">
      <span class="bar"></span>
      <p class="num">3–4%</p>
      <p class="label">OWN LTC INSURANCE</p>
      <p class="body">Of Americans over 50. The gap between who needs it and who has it is staggering.</p>
      <p class="cite">Stroud &amp; Bellamy, QVT Wellness Wire, 2023</p>
    </div>
    <div class="stat-card" style="left:494px;top:452px">
      <span class="bar"></span>
      <p class="num">$700B+</p>
      <p class="label">ANNUAL U.S. LTC COST</p>
      <p class="body">Estimated total long-term care spending — and growing every year.</p>
      <p class="cite">Delacroix Wynn &amp; Pasternak, Civic Ledger Council, 2020</p>
    </div>
    <div class="stat-card" style="left:64px;top:608px;height:140px">
      <span class="bar"></span>
      <p class="num">$470B</p>
      <p class="label">UNPAID FAMILY CARE</p>
      <p class="body">The annual value of care provided by family — measured in time, stress, sacrifice.</p>
      <p class="cite">Tillman &amp; Osei, Meridian Bureau</p>
    </div>
    <div class="stat-card" style="left:494px;top:608px;height:140px">
      <span class="bar"></span>
      <p class="num">80%</p>
      <p class="label">GOES TO RETIREES</p>
      <p class="body">Of total LTC spending. Not a young person's problem — but the time to plan is now.</p>
      <p class="cite">Tillman &amp; Osei, Meridian Bureau</p>
    </div>

    <div class="impact">
      <p class="head serif">Long-term care doesn't just cost money. It costs families.</p>
      <p class="body">Without a plan, the people you love absorb the impact — financially, emotionally, physically. Retirement savings disappear in months. Dignity becomes a daily negotiation.</p>
    </div>

    <p class="sol-eyebrow eyebrow">The solution</p>
    <h2 class="sol-title serif">The Pay Yourself First Principle.</h2>
    <p class="sol-body">Take the first $1, $2, or $3 you earn each day and invest it in permanent life insurance with built-in long-term care<br><b>— underwritten</b><br>by TrueLedger, offered at your group rate, and Guaranteed Issued for everyone.</p>

    <div class="tier" style="left:48px"><p class="rate">$1 / day</p><p class="amt">$20,000</p></div>
    <div class="tier tier--hero" style="left:334px"><p class="rate">$2 / day</p><p class="amt">$40,000</p><p class="tag">★ MOST POPULAR</p></div>
    <div class="tier" style="left:618px"><p class="rate">$3 / day</p><p class="amt">$60,000</p></div>

    <p class="sol-note">Three protections in one: cash value growing ~6% annually, a tax-free death benefit, and LTC coverage that pays 75% of your benefit upfront — tax-free — when you need it most.</p>

    <footer class="r-footer">
      <p class="f-tag serif center">Protect retirement. Preserve dignity. Plan ahead.</p>
      <p class="f-cta center">Look for your personalized offer. Coverage details are coming your way.</p>
      <p class="f-credit center">Brokered by Harbor Perks &nbsp;·&nbsp; Underwritten by TrueLedger &nbsp;·&nbsp; Guaranteed Issued</p>
    </footer>
  </section>

  <section class="flyer flyer--offer" style="width:958px">
    <div class="o-header"></div>
    <div class="o-stripe"></div>
    <p class="o-eyebrow eyebrow center">Your company just upgraded your benefits</p>
    <h1 class="o-title serif center">One small decision.<br>A lifetime of protection.</h1>
    <p class="o-sub center">Permanent life insurance + long-term care coverage, starting at just $1 a day.</p>

    <div class="hero-card">
      <p class="badge">MOST POPULAR</p>
      <p class="pick eyebrow center">Choose your daily investment</p>
      <p class="rate serif center">$2 / day</p>
      <p class="benefit center">$40,000 Life Insurance Benefit</p>
      <p class="note center">Less than your morning coffee. More than peace of mind.</p>
    </div>

    <div class="o-tier" style="left:66px"><p class="rate">$1 / day</p><p class="amt">$20,000 Coverage</p></div>
    <div class="o-tier" style="left:488px"><p class="rate">$3 / day</p><p class="amt">$60,000 Coverage</p></div>

    <h2 class="o-section serif center" style="top:634px">Every Dollar Works Three Ways</h2>

    <div class="way" style="left:66px">
      <p class="head"><span class="dot">1</span>CASH VALUE</p>
      <p class="body">Builds wealth you can borrow against — tax-free.</p>
    </div>
    <div class="way" style="left:347px">
      <p class="head"><span class="dot">2</span>TAX-FREE PAYOUT</p>
      <p class="body">Your family receives the full benefit, income-tax-free.</p>
    </div>
    <div class="way" style="left:628px">
      <p class="head"><span class="dot">3</span>LONG-TERM CARE</p>
      <p class="body">Access your benefit early if you need care later in life.</p>
    </div>

    <h2 class="o-section serif center" style="top:871px">Why This Beats Term Life</h2>

    <div class="compare compare--term">
      <p class="head">TYPICAL TERM LIFE</p>
      <ul>
        <li>Expires after 10–30 years</li>
        <li>No cash value built up</li>
        <li>No long-term care option</li>
        <li>Premiums rise on renewal</li>
      </ul>
    </div>
    <div class="compare compare--plan">
      <p class="head">YOUR NEW PLAN</p>
      <ul>
        <li>Coverage for life — never expires</li>
        <li>Builds cash value you can use</li>
        <li>Long-term care built in</li>
        <li>Rate locked. Forever.</li>
      </ul>
      <svg class="tick" viewBox="0 0 92 92" aria-hidden="true">
        <path d="M80 30 A42 42 0 1 1 62 9" fill="none" stroke="#ffffff" stroke-width="2.5" opacity=".8"/>
        <path d="M26 46 L42 62 L86 14" fill="none" stroke="#ffffff" stroke-width="2.5" opacity=".8"/>
      </svg>
    </div>

    <div class="perk" style="left:66px"><p class="head">RATE LOCKED</p><p class="body">Premium never rises.</p></div>
    <div class="perk" style="left:347px"><p class="head">PORTABLE</p><p class="body small">Yours for life — even if you change jobs.</p></div>
    <div class="perk" style="left:628px"><p class="head">FAMILY COVERAGE</p><p class="body">Add your spouse and children.</p></div>

    <footer class="o-footer">
      <p class="f-tag serif center">Protect retirement. Preserve dignity. Plan ahead.</p>
      <p class="f-cta center">Watch for your personalized coverage details — coming soon.</p>
      <p class="f-credit center">Brokered by Harbor Perks &nbsp;·&nbsp; Underwritten by TrueLedger</p>
    </footer>
  </section>

</div>
</body>
</html>
```